Business Card - Professional Minimalist - Double sided

We appreciate minimalist logo/web/collateral designs that allow design to tell a story. We want to relay a professional image/approach but throwing in a splash of modern when we’re able so long as it’s not distracting. Think 75% classic corporate, 25% modern. Open to black or white design, not sure which might look the best.

Target Market(s)

Senior executives or related government affairs contacts within the agriculture, energy, and defense industries (i.e., potential clients) but located outside of Washington, DC. Most potential clients based in DC with be familiar with both of us and our shared history.

Industry/Entity Type

Consulting

Contact Information for Business Card

Name: Derek M. Holloway
Title: Co-Founder & Partner
Address: 418 Linwood Terrace NE | Suite 2260 | Washington, D.C. 20017
Phone: (202) 555-0148
Email: Derek@BrimleyHolloway.example

Font styles to use
Serif

Colors

Designer to choose only greyscale colors for use in the design.

Requirements
Must have
• Name: Derek M. Holloway
Phone: (202) 555-0148

```html
<!DOCTYPE html>
<html lang="en">
<head>
<meta charset="utf-8">
<title>Brimley Holloway Group – Business Card</title>
<link rel="stylesheet" href="https://fonts.googleapis.com/css2?family=Roboto+Condensed:wght@400;700&display=swap">
<style>
  :root {
    --backdrop: #cfcbc6;
    --card: #e7e4e0;
    --card-edge: #b9b5b0;
    --band-dark: #2e2e30;
    --band-mid: #4a4a4d;
    --name: #b8b8ba;
    --title: #e6e6e6;
    --ink: #1f1f21;
    --icon: #3a3a3c;
  }
  html, body {
    margin: 0;
    padding: 0;
    width: 1200px;
    height: 969px;
    overflow: hidden;
    background: var(--backdrop);
    font-family: "Roboto Condensed", "Arial Narrow", sans-serif;
  }
  .card {
    position: absolute;
    left: 100px;
    top: 200px;
    width: 1000px;
    height: 569px;
    background: var(--card);
    border: 1px solid var(--card-edge);
    border-radius: 0 22px 0 22px;
    box-sizing: border-box;
  }
  .name-band {
    position: absolute;
    left: 0;
    top: 89px;
    width: 443px;
    height: 78px;
    background: linear-gradient(90deg, var(--band-mid), var(--band-dark));
  }
  .person-name {
    position: absolute;
    left: 54px;
    top: 6px;
    margin: 0;
    font-size: 31px;
    font-weight: 700;
    color: var(--name);
    letter-spacing: 0.3px;
  }
  .person-title {
    position: absolute;
    left: 54px;
    top: 45px;
    margin: 0;
    font-size: 20px;
    font-weight: 400;
    color: var(--title);
  }
  .brand {
    position: absolute;
    right: 64px;
    top: 100px;
    display: flex;
    align-items: center;
    gap: 12px;
  }
  .brand-square {
    width: 30px;
    height: 30px;
    background: var(--ink);
  }
  .brand-name {
    font-size: 30px;
    font-weight: 700;
    color: var(--ink);
    text-transform: uppercase;
    letter-spacing: 0.5px;
  }
  .contact-list {
    position: absolute;
    left: 54px;
    top: 424px;
    margin: 0;
    padding: 0;
    list-style: none;
  }
  .contact-list li {
    display: flex;
    align-items: center;
    height: 28px;
    font-size: 22px;
    color: var(--ink);
  }
  .contact-list svg {
    width: 16px;
    height: 16px;
    margin-right: 14px;
    fill: var(--icon);
  }
  .office-address {
    position: absolute;
    right: 64px;
    top: 424px;
    margin: 0;
    text-align: right;
    font-style: normal;
    font-size: 22px;
    line-height: 28px;
    color: var(--ink);
  }
</style>
</head>
<body>
  <div class="card">
    <div class="name-band">
      <h1 class="person-name">Derek M. Holloway</h1>
      <p class="person-title">Co-Founder &amp; Partner</p>
    </div>

    <div class="brand">
      <span class="brand-square"></span>
      <span class="brand-name">Brimley Holloway Group</span>
    </div>

    <ul class="contact-list">
      <li>
        <svg viewBox="0 0 16 16" aria-hidden="true"><path d="M3.6 1.2l2.3 2.6-1.2 1.9c.9 2 2.6 3.7 4.6 4.6l1.9-1.2 2.6 2.3-1.4 2.4C7.2 14 2 8.8 1.2 3.6z"/></svg>
        (202) 555-0148
      </li>
      <li>
        <svg viewBox="0 0 16 16" aria-hidden="true"><path d="M1 3.5h14v9H1z M1.8 4.3L8 9l6.2-4.7" stroke="#e7e4e0" stroke-width="1"/></svg>
        Derek@BrimleyHolloway.example
      </li>
      <li>
        <svg viewBox="0 0 16 16" aria-hidden="true"><circle cx="8" cy="8" r="7"/><path d="M4 5c2 0 3 1 2.5 2.5S7 10 5.5 11M10 3c-.5 1.5.5 2.5 2 2.5M9.5 13c0-2 1-3 3-3" stroke="#e7e4e0" stroke-width="1.2" fill="none"/></svg>
        www.BrimleyHolloway.example
      </li>
    </ul>

    <address class="office-address">
      Brimley Holloway Group LLC<br>
      418 Linwood Terrace NE<br>
      Suite 2260, Washington, D.C. 20017
    </address>
  </div>
</body>
</html>
```